GDFH Business Card

Looking for a business card design to incorporate our branding. We want to only use the colors listing in the Branding Package (attached).
Updates

Target Market(s)

People who need their phone or device fixed.

Industry/Entity Type

Electronics

Contact Information for Business Card

Please use:

Gadget Fix Haven LLC
4870 S Ridgecrest Pkwy
Suite 318
San Antonio, TX 78291

Wendell Thorsby, Store Manager

(210) 555-0147

Requirements
Must have
• Must include the colors that are contained within the Branding Package PDF file.

```html
<!DOCTYPE html>
<html lang="en">
<head>
<meta charset="utf-8">
<title>GDFH Business Card</title>
<link rel="stylesheet" href="https://fonts.googleapis.com/css2?family=Open+Sans:wght@400;700&display=swap">
<style>
  :root {
    --brand-orange: #ef5a24;
    --ink-grey: #4a4a4a;
    --card-white: #ffffff;
    --stage: #e9e6e2;
  }
  * { margin: 0; padding: 0; box-sizing: border-box; }
  html, body { width: 1200px; height: 1000px; overflow: hidden; }
  body {
    background: var(--stage);
    font-family: "Open Sans", Arial, sans-serif;
    position: relative;
  }
  .card {
    position: absolute;
    left: 266px;
    width: 666px;
    height: 397px;
    border-radius: 24px;
  }
  .card--front { top: 74px; background: var(--card-white); }
  .card--back { top: 533px; background: var(--brand-orange); }

  .brand {
    position: absolute;
    left: 0; right: 0;
    display: flex;
    align-items: center;
    justify-content: center;
    gap: 22px;
  }
  .card--front .brand { top: 78px; }
  .card--back .brand { top: 152px; }
  .brand__square {
    width: 86px; height: 86px;
    border-radius: 14px;
  }
  .card--front .brand__square { background: var(--brand-orange); }
  .card--back .brand__square { border: 4px solid var(--card-white); }
  .brand__name {
    font-size: 44px;
    font-weight: 400;
    letter-spacing: 0.5px;
  }
  .card--front .brand__name { color: var(--brand-orange); }
  .card--back .brand__name { color: var(--card-white); }

  .identity {
    position: absolute;
    right: 352px;
    top: 248px;
    text-align: right;
    color: var(--ink-grey);
    font-size: 16px;
    line-height: 21px;
  }
  .identity__name {
    color: var(--brand-orange);
    font-weight: 700;
    font-size: 20px;
    letter-spacing: 0.3px;
    line-height: 26px;
  }
  .identity__title { margin-bottom: 13px; }

  .divider {
    position: absolute;
    left: 331px;
    top: 251px;
    width: 2px;
    height: 93px;
    background: var(--brand-orange);
  }

  .contact {
    position: absolute;
    left: 348px;
    top: 248px;
    list-style: none;
    color: var(--ink-grey);
    font-size: 16px;
  }
  .contact__item {
    display: flex;
    align-items: center;
    gap: 6px;
    height: 25.5px;
  }
  .contact__icon { width: 15px; height: 15px; fill: var(--brand-orange); flex: none; }
</style>
</head>
<body>
  <section class="card card--front">
    <div class="brand">
      <div class="brand__square"></div>
      <div class="brand__name">Gadget Fix Haven</div>
    </div>

    <div class="identity">
      <div class="identity__name">WENDELL THORSBY</div>
      <div class="identity__title">Store Manager</div>
      <div class="identity__address">4870 S Ridgecrest Pkwy, Suite 318</div>
      <div class="identity__address">San Antonio, TX 78291</div>
    </div>

    <div class="divider"></div>

    <ul class="contact">
      <li class="contact__item">
        <svg class="contact__icon" viewBox="0 0 16 16"><path d="M1 5c0-2 3-3 7-3s7 1 7 3v1.5h-4V5H5v1.5H1z"/><path d="M4 8h8l2 6H2z"/></svg>
        <span>(210) 555-0147</span>
      </li>
      <li class="contact__item">
        <svg class="contact__icon" viewBox="0 0 16 16"><rect x="4" y="1" width="8" height="4"/><rect x="1" y="6" width="14" height="6" rx="1"/><rect x="4" y="10" width="8" height="5"/></svg>
        <span>(210) 555-0148</span>
      </li>
      <li class="contact__item">
        <svg class="contact__icon" viewBox="0 0 16 16"><path d="M1 3h14v10H1z"/><path d="M1.5 3.5 8 9l6.5-5.5" fill="none" stroke="#fff" stroke-width="1.4"/></svg>
        <span>info@gadgetfixhaven.com</span>
      </li>
      <li class="contact__item">
        <svg class="contact__icon" viewBox="0 0 16 16"><circle cx="8" cy="8" r="7"/><path d="M1 8h14M8 1c-3 3-3 11 0 14M8 1c3 3 3 11 0 14" fill="none" stroke="#fff" stroke-width="1"/></svg>
        <span>www.gadgetfixhaven.com</span>
      </li>
    </ul>
  </section>

  <section class="card card--back" role="img" aria-label="Orange card back with a faint repeating brand pattern and the Gadget Fix Haven name">
    <div class="brand">
      <div class="brand__square"></div>
      <div class="brand__name">Gadget Fix Haven</div>
    </div>
  </section>
</body>
</html>
```